Need a book cover design for a Lumora Book on Herbal Remedies

I need a book cover for my new ebook, here are the details:
Title: Meadow Cures
Sub-Heading: Buried Ancient Garden Tonics
Reclaiming the Wisdom of Roots for Everyday Wellness and Strength
Author: Nora Belcourt

```html
<!DOCTYPE html>
<html lang="en">
<head>
<meta charset="utf-8">
<title>Meadow Cures — Nora Belcourt</title>
<link rel="stylesheet" href="https://fonts.googleapis.com/css2?family=Anton&family=Itim&display=swap">
<style>
  :root {
    --parchment-light: #e9dca6;
    --parchment-mid: #d8c58a;
    --parchment-dark: #b89a5c;
    --roll-light: #e2d29c;
    --roll-dark: #a88850;
    --ink-brown: #3a2519;
    --title-brown: #4a3020;
    --herb-green: #3f8a35;
    --wood-dark: #4a3d33;
    --wood-mid: #6e5d4e;
  }
  html, body {
    margin: 0;
    padding: 0;
    width: 750px;
    height: 1200px;
    overflow: hidden;
    background: #ffffff;
  }
  .cover {
    position: relative;
    width: 750px;
    height: 1200px;
    overflow: hidden;
    background: var(--wood-dark);
  }
  .herb-table {
    position: absolute;
    left: 470px;
    top: 0;
    width: 280px;
    height: 1200px;
    background:
      radial-gradient(ellipse 110px 95px at 150px 270px, #b88a5e 0%, #9a7098 45%, transparent 75%),
      radial-gradient(ellipse 95px 85px at 150px 470px, #c27a5a 0%, #b94a5e 45%, transparent 75%),
      radial-gradient(ellipse 95px 85px at 140px 650px, #b27a52 0%, #8f5a3e 45%, transparent 75%),
      radial-gradient(ellipse 95px 85px at 140px 830px, #b07c58 0%, #9a9486 45%, transparent 75%),
      radial-gradient(ellipse 90px 80px at 150px 1000px, #c99a6c 0%, #d8c3a0 45%, transparent 75%),
      linear-gradient(90deg, var(--wood-dark), var(--wood-mid) 50%, var(--wood-dark));
  }
  .scroll {
    position: absolute;
    left: 0;
    top: 0;
    width: 500px;
    height: 1200px;
  }
  .scroll-sheet {
    position: absolute;
    left: 0;
    top: 110px;
    width: 490px;
    height: 945px;
    background:
      radial-gradient(ellipse at 45% 50%, var(--parchment-light) 0%, var(--parchment-mid) 65%, var(--parchment-dark) 100%);
  }
  .scroll-roll {
    position: absolute;
    left: 0;
    width: 520px;
    background: linear-gradient(180deg, var(--roll-dark) 0%, var(--roll-light) 30%, var(--parchment-mid) 70%, var(--roll-dark) 100%);
  }
  .scroll-roll--top { top: 0; height: 128px; }
  .scroll-roll--bottom { top: 1040px; height: 160px; }
  .title {
    position: absolute;
    left: 40px;
    top: 258px;
    width: 410px;
    margin: 0;
    font-family: "Anton", "Impact", sans-serif;
    font-weight: 400;
    font-size: 168px;
    line-height: 146px;
    letter-spacing: 2px;
    color: var(--title-brown);
    text-transform: uppercase;
    text-align: center;
  }
  .title-line {
    display: block;
    white-space: nowrap;
    transform-origin: center;
  }
  .title-line--first { transform: scaleX(0.68); }
  .title-line--second { transform: scaleX(1); }
  .subtitle {
    position: absolute;
    left: 20px;
    top: 596px;
    width: 470px;
    margin: 0;
    font-family: "Itim", "Comic Sans MS", sans-serif;
    font-size: 40px;
    line-height: 60px;
    color: var(--herb-green);
    text-transform: uppercase;
    letter-spacing: 1px;
    text-align: center;
  }
  .tagline {
    position: absolute;
    left: 20px;
    top: 722px;
    width: 440px;
    margin: 0;
    font-family: "Itim", "Comic Sans MS", sans-serif;
    font-size: 31px;
    line-height: 56px;
    color: var(--ink-brown);
    text-align: center;
  }
  .author {
    position: absolute;
    left: 20px;
    top: 1110px;
    width: 440px;
    margin: 0;
    font-family: "Itim", "Comic Sans MS", sans-serif;
    font-size: 38px;
    letter-spacing: 1px;
    color: var(--ink-brown);
    text-transform: uppercase;
    text-align: center;
  }
</style>
</head>
<body>
<main class="cover">
  <div class="herb-table" role="img" aria-label="Wooden table with a mortar and pestle and small wooden bowls of dried lavender, red clover blossoms, rosebuds and herbs"></div>
  <div class="scroll" role="img" aria-label="Aged parchment scroll">
    <div class="scroll-sheet"></div>
    <div class="scroll-roll scroll-roll--top"></div>
    <div class="scroll-roll scroll-roll--bottom"></div>
  </div>
  <h1 class="title"><span class="title-line title-line--first">Meadow</span><span class="title-line title-line--second">Cures</span></h1>
  <h2 class="subtitle">Buried Ancient<br>Garden Tonics</h2>
  <p class="tagline">Reclaiming the Wisdom of<br>Roots for Everyday<br>Wellness and<br>Strength</p>
  <p class="author">Nora Belcourt</p>
</main>
</body>
</html>
```